Website Design for Law Firm

We need a fresh new website design for our client 'Vendrick Legal' who specialises as a Criminal, Traffic & Civil Lawyer in Perth, Western Australia. We are looking for a very clean, professional and elegant look for the website, a presence of power and class needed as he deals with high end clients. Black, Silver and hints of gold need to run through the design without making the site look too dark. We are after a very modern, spacious web look, use of large readable text with links to social media (such as Chatterloom, Zumbly+, Quibbr, WorkMesh) to stand out and his contact details to be made very predominate.

Reason: Public holidays here in Australia, need more business hours to discuss designs with client.

Reason: Client needs more time to look through designs.

Reason: Client is going over last of designs. Design will be picked early next week!

Industry/Entity Type

Law Firm

```html
<!DOCTYPE html>
<html lang="en">
<head>
<meta charset="utf-8">
<title>Vendrick Legal</title>
<link href="https://fonts.googleapis.com/css2?family=Arimo:wght@400;700&display=swap" rel="stylesheet">
<style>
:root{
  --ink:#1b1b1b;
  --text:#3a3a3a;
  --muted:#555;
  --brown:#5a3026;
  --page-top:#6e6e6e;
  --page-top-light:#a9a9a9;
  --page:#efeef0;
  --header:#dcdcdc;
  --panel:#f3f2f4;
  --line:#cfcfcf;
  --footer:#000;
  --white:#fff;
}
*{box-sizing:border-box;margin:0;padding:0}
html,body{width:1200px;height:943px;overflow:hidden}
body{position:relative;font-family:"Arimo",Arial,sans-serif;color:var(--text);background:var(--page)}
.abs{position:absolute}
.top-band{left:0;top:0;width:1200px;height:251px;background:linear-gradient(var(--page-top),var(--page-top-light))}
.site-footer{left:0;top:847px;width:1200px;height:96px;background:var(--footer);color:var(--white);font-size:11px;z-index:1}
.container{left:164px;top:40px;width:875px;height:831px;background:#f1f0f2;border-radius:6px;box-shadow:0 2px 10px rgba(0,0,0,.35);overflow:hidden;z-index:2}
.header{left:0;top:0;width:875px;height:122px;background:linear-gradient(#e6e6e6,var(--header))}
.logo{left:24px;top:34px;display:flex;align-items:center;gap:10px;font-size:30px;font-weight:700;color:var(--ink);letter-spacing:1px}
.logo-mark{width:26px;height:26px;background:var(--ink)}
.search{left:679px;top:50px;width:167px;height:26px;background:var(--white);border:1px solid #c8c8c8;border-radius:3px;font-size:11px;font-style:italic;color:#333;padding:6px 8px}
.search svg{position:absolute;right:6px;top:3px}
.date{right:28px;top:94px;font-size:13px;color:#333}
.nav{left:0;top:122px;width:875px;height:40px;display:flex;background:linear-gradient(#fafafa,#e6e6e6);border-bottom:1px solid #d0d0d0}
.nav a{display:flex;align-items:center;justify-content:center;font-size:11px;color:#333;text-decoration:none;border-right:1px solid #d2d2d2;white-space:nowrap}
.slider{left:10px;top:176px;width:588px;height:254px;background:var(--white);border:1px solid #ccc}
.slide-photo{left:5px;top:5px;width:576px;height:242px;background:linear-gradient(100deg,#7b5c47 0%,#b89a80 30%,#3c3b44 60%,#6a5a4d 100%)}
.dots{right:12px;bottom:14px;display:flex;gap:4px}
.dots span{width:12px;height:8px;background:#bbb}
.dots span:first-child{background:var(--white)}
.slider-shadow{left:20px;top:432px;width:570px;height:18px;background:radial-gradient(ellipse at top,rgba(0,0,0,.35),transparent 70%)}
.arrows{left:291px;top:440px;display:flex;gap:2px}
.arrows span{width:19px;height:23px;background:#c9c9c9;border-radius:3px;display:flex;align-items:center;justify-content:center}
.welcome{left:52px;top:468px;font-size:21px;font-weight:400;color:#222}
.rule{left:48px;top:505px;width:508px;height:1px;background:var(--line)}
.intro{left:52px;top:529px;width:470px;font-size:11.5px;line-height:14.5px;color:#333;text-indent:26px}
.btn{background:var(--brown);color:var(--white);border-radius:3px;display:flex;align-items:center;justify-content:center;font-size:11px}
.intro-btn{left:430px;top:615px;width:96px;height:27px}
.card{top:673px;width:191px;height:145px;background:#f6f5f7;border:1px solid #d4d4d4;border-radius:4px}
.card-photo{left:6px;top:8px;width:173px;height:78px}
.card h3{position:absolute;left:8px;top:92px;font-size:12px;font-weight:400;color:#222}
.card p{position:absolute;left:8px;top:110px;width:110px;font-size:9.5px;line-height:12px;color:#333}
.card .btn{position:absolute;right:10px;top:112px;width:56px;height:21px;font-size:10px}
.panel{left:607px;width:257px;background:var(--panel);border:1px solid #d2d2d2;border-radius:4px;overflow:hidden}
.panel-head{height:34px;background:linear-gradient(#e9e9e9,#cfcfcf);display:flex;align-items:center;justify-content:space-between;padding:0 12px;font-size:12.5px;color:#333}
.panel-toggle{width:20px;height:18px;background:#444;border-radius:2px;display:flex;align-items:center;justify-content:center}
.field-label{font-size:10px;color:#333;left:13px}
.field{left:116px;width:126px;height:21px;background:var(--white);border:1px solid #c6c6c6;border-radius:3px}
.post{left:13px;width:232px;height:72px;border-bottom:1px solid #ddd}
.post-photo{left:0;top:0;width:58px;height:58px;border:2px solid var(--white);box-shadow:0 0 2px #999}
.post h4{position:absolute;left:72px;top:2px;font-size:10px;color:#222}
.post time{position:absolute;left:72px;top:15px;font-size:10px;color:#333}
.post p{position:absolute;left:72px;top:27px;width:162px;font-size:10px;line-height:12px;color:#444}
.view-all{right:12px;top:288px;font-size:10.5px;color:#c0392b;text-decoration:underline}
.newsletter-note{text-align:center;font-size:11px;line-height:14px;color:#333;margin-top:5px}
.footer-nav{left:0;top:30px;width:1200px;display:flex;justify-content:center;gap:18px}
.footer-nav span.sep{color:#aaa}
.copyright{left:0;top:64px;width:1200px;text-align:center}
</style>
</head>
<body>
<div class="abs top-band"></div>

<footer class="abs site-footer">
  <div class="abs footer-nav">
    <span>Home</span><span class="sep">|</span><span>About Us</span><span class="sep">|</span><span>Practice Areas</span><span class="sep">|</span><span>Scope Of Advice</span><span class="sep">|</span><span>Legal Costs</span><span class="sep">|</span><span>Press</span><span class="sep">|</span><span>Recent Cases</span><span class="sep">|</span><span>FAQ</span><span class="sep">|</span><span>Links</span><span class="sep">|</span><span>Contact</span><span class="sep">|</span><span>Policy</span>
  </div>
  <div class="abs copyright">Copyright &copy; 2014, Vendricklegal.com. All rights reserved.</div>
</footer>

<div class="abs container">
  <header class="abs header">
    <div class="abs logo"><span class="logo-mark"></span>VENDRICK LEGAL</div>
    <div class="abs search">Search
      <svg width="22" height="20" viewBox="0 0 22 20"><circle cx="8" cy="8" r="5.5" fill="none" stroke="#2c5aa0" stroke-width="2.5"/><line x1="12" y1="12" x2="19" y2="18" stroke="#2c5aa0" stroke-width="3" stroke-linecap="round"/></svg>
    </div>
    <div class="abs date">Wednesday, 8th February, 2014</div>
  </header>

  <nav class="abs nav">
    <a style="width:55px">HOME</a><a style="width:78px">ABOUT US</a><a style="width:113px">PRACTICE AREAS</a><a style="width:117px">SCOPE OF ADVICE</a><a style="width:92px">LEGAL COSTS</a><a style="width:56px">PRESS</a><a style="width:107px">RECENT CASES</a><a style="width:41px">FAQ</a><a style="width:51px">LINKS</a><a style="width:79px">CONTACT</a><a style="width:86px;border-right:0">POLICY</a>
  </nav>

  <div class="abs slider">
    <div class="abs slide-photo" role="img" aria-label="Photo of a smiling team of lawyers in business suits in an office"></div>
    <div class="abs dots"><span></span><span></span><span></span><span></span><span></span></div>
  </div>
  <div class="abs slider-shadow"></div>
  <div class="abs arrows">
    <span><svg width="8" height="10"><path d="M6 1L2 5l4 4" fill="none" stroke="#fff" stroke-width="2"/></svg></span>
    <span><svg width="8" height="10"><path d="M2 1l4 4-4 4" fill="none" stroke="#fff" stroke-width="2"/></svg></span>
  </div>

  <h1 class="abs welcome">Welcome To Our Site!</h1>
  <div class="abs rule"></div>
  <p class="abs intro">Lorem ipsum dolor sit amet, consectetuer adipiscing elit. sed diem nonumy in eu nulles gravida neque. Nulla gravida vestibulum metis a acumsan, aliquam in sagittis ut. Solicitudin sed massa ud enim veniam. Curabitur tempus sem vitae mi vestibulum volut pat malesuada erat vestibulum. Sed aliquam dolor at dolor consequat gravida. Fusce mi neque tempus nec fequat sit amet . Tincidunt ut leo. Nam semper omare enim.</p>
  <div class="abs btn intro-btn">Read more</div>

  <div class="abs card" style="left:10px">
    <div class="abs card-photo" role="img" aria-label="Photo of handcuffed hands in front of a suit" style="background:linear-gradient(90deg,#c89a78,#7a3a2a 50%,#c29274)"></div>
    <h3>CRIMINAL LAWYER</h3><p>Lorem ipsum dolor sit amet consectetur adi...</p><div class="btn">read more</div>
  </div>
  <div class="abs card" style="left:207px">
    <div class="abs card-photo" role="img" aria-label="Photo of a traffic police officer raising a hand" style="background:linear-gradient(90deg,#3c5a86,#6d7f99 50%,#2e4a78)"></div>
    <h3>TRAFFIC LAWYER</h3><p>Lorem ipsum dolor sit amet consectetur adi...</p><div class="btn">read more</div>
  </div>
  <div class="abs card" style="left:406px">
    <div class="abs card-photo" role="img" aria-label="Photo of a judge's gavel resting on law books" style="background:linear-gradient(90deg,#efe7dc,#8a5a38 50%,#e6dccd)"></div>
    <h3>CIVIL LAWYER</h3><p>Lorem ipsum dolor sit amet consectetur adi...</p><div class="btn">read more</div>
  </div>

  <section class="abs panel" style="top:176px;height:205px">
    <div class="panel-head">CONTACT US<span class="panel-toggle"><svg width="8" height="6"><path d="M0 0h8L4 6z" fill="#ddd"/></svg></span></div>
    <span class="abs field-label" style="top:50px">Name</span><div class="abs field" style="top:45px"></div>
    <span class="abs field-label" style="top:75px">Email</span><div class="abs field" style="top:69px"></div>
    <span class="abs field-label" style="top:98px">Phone</span><div class="abs field" style="top:93px"></div>
    <span class="abs field-label" style="top:122px">Message</span><div class="abs field" style="top:117px;height:51px"></div>
    <div class="abs btn" style="left:159px;top:177px;width:73px;height:19px">SUBMIT</div>
  </section>

  <section class="abs panel" style="top:391px;height:305px">
    <div class="panel-head">RECENT POST<span class="panel-toggle"><svg width="8" height="6"><path d="M0 0h8L4 6z" fill="#ddd"/></svg></span></div>
    <article class="abs post" style="top:43px">
      <div class="abs post-photo" role="img" aria-label="Photo of lawyers shaking hands" style="background:linear-gradient(135deg,#3b3f4a,#a08a78)"></div>
      <h4>Lorem ipsum dolor sit amet</h4><time>January, 15th 2014</time><p>Lorem ipsum dolor sit amet,conse cteteur adipiscing elit. set</p>
    </article>
    <article class="abs post" style="top:124px">
      <div class="abs post-photo" role="img" aria-label="Photo of a business meeting" style="background:linear-gradient(135deg,#6b5a4c,#c2a88e)"></div>
      <h4>Lorem ipsum dolor sit amet.</h4><time>February 17th 2014</time><p>Lorem ipsum dolor sit amet,conse cteteur adipiscing elit. set</p>
    </article>
    <article class="abs post" style="top:206px">
      <div class="abs post-photo" role="img" aria-label="Photo of a client consultation at a desk" style="background:linear-gradient(135deg,#5e7384,#c8c2b8)"></div>
      <h4>Lorem ipsum dolor sit amet</h4><time>March, 22th 2014</time><p>Lorem ipsum dolor sit amet,conse cteteur adipiscing elit. set</p>
    </article>
    <a class="abs view-all">View All</a>
  </section>

  <section class="abs panel" style="top:708px;height:102px">
    <div class="panel-head">NEWSLETTER<span class="panel-toggle"><svg width="8" height="6"><path d="M0 0h8L4 6z" fill="#ddd"/></svg></span></div>
    <p class="newsletter-note">to receive our newsletter regarding events<br>and seminar please sign up</p>
    <div class="abs field" style="left:15px;top:73px;width:148px;height:20px;font-size:10px;padding:4px 6px;color:#444">Your email address</div>
    <div class="abs btn" style="left:168px;top:73px;width:73px;height:20px">Submit</div>
  </section>
</div>
</body>
</html>
```